Fore Sale sign for my real estate agency

I am a Brisbane - Australia inner western suburbs boutique real estate agent who is needing a for sale sign. We are a small dynamic family agency that needs a for sale sign that will standout and give us a strong presence in the market.

I have attached a logo I like, however I am not fixed on anything and am open to suggestions.

The information on the sign should contain but not necessarily limited to the following information - please appreciate I am very open
1 logo - O'Venny
2 Ph number - 3847 1952
3 web address - ovenny.com.au

Thank you
Gareth O'Venny

```html
<!DOCTYPE html>
<html lang="en">
<head>
<meta charset="UTF-8">
<title>O'Venny For Sale Signs</title>
<link href="https://fonts.googleapis.com/css2?family=Arimo:wght@400;700&family=Archivo+Narrow:wght@400&display=swap" rel="stylesheet">
<style>
  :root {
    --ink: #231f20;
    --orange: #f7931e;
    --white: #ffffff;
    --backdrop: #e6e6e6;
  }
  * { box-sizing: border-box; margin: 0; padding: 0; }
  html, body {
    width: 1200px;
    height: 900px;
    overflow: hidden;
    background: var(--backdrop);
    font-family: "Arimo", Arial, sans-serif;
  }
  .sign {
    position: absolute;
    border: 12px solid var(--ink);
    background: var(--ink);
    display: grid;
  }
  .sign--right-arrow {
    left: 45px; top: 127px;
    width: 525px; height: 395px;
    grid-template-rows: 209px 157px;
    row-gap: 5px;
  }
  .sign--left-arrow {
    left: 620px; top: 342px;
    width: 545px; height: 408px;
    grid-template-rows: 216px 162px;
    row-gap: 6px;
  }
  .brand-panel {
    background: var(--white);
    display: flex;
    align-items: center;
    justify-content: center;
    gap: 14px;
  }
  .brand-name {
    font-weight: 700;
    font-size: 98px;
    letter-spacing: -1px;
    color: var(--ink);
    line-height: 1;
  }
  .brand-square {
    width: 22px; height: 22px;
    background: var(--orange);
    align-self: flex-end;
    margin-bottom: 52px;
  }
  .info-row {
    display: grid;
    column-gap: 5px;
  }
  .sign--right-arrow .info-row { grid-template-columns: 319px 1fr; }
  .sign--left-arrow .info-row { grid-template-columns: 185px 1fr; }
  .contact-panel {
    background: var(--orange);
    color: var(--white);
    display: flex;
    flex-direction: column;
    justify-content: center;
    padding-left: 12px;
  }
  .broker-name {
    font-family: "Archivo Narrow", "Arial Narrow", sans-serif;
    font-size: 29px;
    line-height: 1.05;
  }
  .phone {
    font-weight: 700;
    font-size: 55px;
    line-height: 1.05;
    letter-spacing: -1px;
  }
  .web {
    font-size: 33px;
    line-height: 1.05;
  }
  .status-panel {
    background: var(--white);
    color: var(--ink);
    display: flex;
    flex-direction: column;
    align-items: center;
    justify-content: center;
    font-weight: 700;
    line-height: 0.95;
  }
  .status-for { font-size: 31px; }
  .status-sale { font-size: 48px; margin-bottom: 8px; }
  .direction-arrow { width: 160px; height: 50px; }
</style>
</head>
<body>

  <section class="sign sign--right-arrow">
    <div class="brand-panel">
      <span class="brand-name">O'Venny</span>
      <span class="brand-square"></span>
    </div>
    <div class="info-row">
      <div class="contact-panel">
        <p class="broker-name">Xxxxx Xxxxx, Broker</p>
        <p class="phone">3847 1952</p>
        <p class="web">ovenny.com.au</p>
      </div>
      <div class="status-panel">
        <span class="status-for">FOR</span>
        <span class="status-sale">SALE</span>
        <svg class="direction-arrow" viewBox="0 0 160 50" aria-hidden="true">
          <g fill="#f7931e">
            <rect x="0" y="15" width="5" height="20"/>
            <rect x="8" y="15" width="5" height="20"/>
            <rect x="16" y="15" width="5" height="20"/>
            <rect x="24" y="15" width="5" height="20"/>
            <rect x="32" y="15" width="90" height="20"/>
            <polygon points="120,2 160,25 120,48"/>
          </g>
        </svg>
      </div>
    </div>
  </section>

  <section class="sign sign--left-arrow">
    <div class="brand-panel">
      <span class="brand-name">O'Venny</span>
      <span class="brand-square"></span>
    </div>
    <div class="info-row">
      <div class="status-panel">
        <span class="status-for">FOR</span>
        <span class="status-sale">SALE</span>
        <svg class="direction-arrow" viewBox="0 0 160 50" aria-hidden="true">
          <g fill="#f7931e">
            <polygon points="40,2 0,25 40,48"/>
            <rect x="38" y="15" width="90" height="20"/>
            <rect x="131" y="15" width="5" height="20"/>
            <rect x="139" y="15" width="5" height="20"/>
            <rect x="147" y="15" width="5" height="20"/>
            <rect x="155" y="15" width="5" height="20"/>
          </g>
        </svg>
      </div>
      <div class="contact-panel">
        <p class="broker-name">Xxxxx Xxxxx, Broker</p>
        <p class="phone">3847 1952</p>
        <p class="web">ovenny.com.au</p>
      </div>
    </div>
  </section>

</body>
</html>
```